12-page Product Brochure for School Archiving Specialist Company

We require a 12-page brochure for our company based in Melbourne, VIC. Our company specializes in tailored archiving solutions for Australian schools of all sizes, and our main product is the "Tidy Vault" archiving system.
We have a ready-to-use brochure structure that can help designers get a better idea of what we're looking for in the final brochure. We will also provide imagery, graphics, and copy that will be used in the brochure - designers will just have to piece them all together and add their own touch of flair to it!
We are looking for the design to clearly communicate what we we do from a product, service and system perspective. The design should inspire trust, be clear and concise, but also to incorporate the fun spirit that embodies our company and our mascots, Pemmo and Roddy.
Attached is a suggested brochure structure, previous brochures we have had designed, a project brief, as well as examples of what we like.
Company Name: Tidy Vault (operating under Bramwell Filing Group)
Company Location: Melbourne, Victoria, Australia
Contacts: niall@bramwellfilinggroup.com.au / desmond@bramwellfilinggroup.com.au
Project Type: 12-page A4 Brochure
Project Goal: A brochure that clearly communicates what we do from a product, service, and system perspective. The design should inspire trust, be clear and concise, but should also incorporate the fun spirit that embodies our company and our mascots, Pemmo and Roddi.
Final Output Format: .PDF and .AI or .INDD
Project Details and Scope of Work: We require a 14-page A4 brochure for our company based in Melbourne, VIC. Our company specializes in tailored archiving solutions for Australian schools of all sizes, and our main product is the "Tidy Vault" archiving system. We have a ready-to-use brochure structure that can help designers get a better idea of what we're looking for in the final brochure. We will also provide imagery, graphics, and copy that will be used in the brochure - designers will just have to piece them all together, fill in any gaps, and add their own touch of flair to it!
Links to Existing Content:
Graphics/Imagery*: https://files.example-share.net/folders/a7Kq2mT9xR4vLp8Wn3Zc
Brochure Copy:
https://files.example-share.net/docs/b3Hn8sV1yQ6tMd5Xk2Je
Photos:
https://files.example-share.net/folders/c9Pw4fL7uB2rNg6Ys1Dh
Previous Tidy Vault Brochures and Best Practice Design Examples Pages**:
https://files.example-share.net/folders/d5Tm3jR8oC1wKe7Vb4Fq
* Each folder, named after different sections of the brochure, contains graphics we would like to be used for that corresponding page/section.
** The photos in each folder are examples. Please refer to the Brochure Photo Folder for all options.
Target Market(s)
Schools of all sizes in Australia
Industry/Entity Type
Archiving / Storage
Look and feel

```html
<!DOCTYPE html>
<html lang="en">
<head>
<meta charset="utf-8">
<title>Tidy Vault – Problem</title>
<link rel="stylesheet" href="https://fonts.googleapis.com/css2?family=Montserrat:wght@700;800;900&display=swap">
<style>
  :root {
    --navy: #2e3b56;
    --navy-deep: #253049;
    --red: #e3232d;
    --red-dark: #a3141b;
    --white: #ffffff;
    --photo-light: #c9b89a;
    --photo-dark: #7d6e58;
  }
  * { margin: 0; padding: 0; box-sizing: border-box; }
  html, body { width: 848px; height: 1200px; overflow: hidden; background: var(--navy); }
  .page {
    position: relative;
    width: 848px;
    height: 1200px;
    background: var(--navy);
    font-family: "Montserrat", Arial, sans-serif;
    overflow: hidden;
  }
  .artwork { position: absolute; inset: 0; width: 848px; height: 1200px; }
  .mascot-scene {
    position: absolute;
    left: 0; top: 121px;
    width: 306px; height: 252px;
    background: radial-gradient(ellipse at 45% 55%, #c7ad86 0%, #9a8767 45%, rgba(46,59,86,0) 75%);
  }
  .brand {
    position: absolute;
    right: 26px; top: 36px;
    display: flex; align-items: center; gap: 10px;
    color: var(--white);
    font-weight: 800;
    font-size: 32px;
    letter-spacing: 0.5px;
  }
  .brand-mark { width: 26px; height: 26px; background: var(--white); }
  .section-title {
    position: absolute;
    left: 290px; top: 208px;
    color: var(--white);
    font-weight: 900;
    font-size: 64px;
    line-height: 74px;
    letter-spacing: 1px;
  }
  .problem-list { list-style: none; }
  .problem-item {
    position: absolute;
    color: var(--white);
    font-weight: 700;
    font-size: 15px;
    line-height: 22px;
    white-space: nowrap;
  }
</style>
</head>
<body>
<main class="page">
  <svg class="artwork" viewBox="0 0 595 842" preserveAspectRatio="none" aria-hidden="false">
    <defs>
      <linearGradient id="photoTone" x1="0" y1="0" x2="1" y2="1">
        <stop offset="0" stop-color="#8a7a62"/>
        <stop offset="0.45" stop-color="#cdbb9c"/>
        <stop offset="1" stop-color="#6f665a"/>
      </linearGradient>
    </defs>
    <polygon class="storage-photo" role="img" aria-label="Photo of a storeroom piled with collapsing archive boxes"
             points="0,0 595,0 595,672 482,672 175,130 0,130" fill="url(#photoTone)"/>
    <line class="photo-edge" x1="175" y1="130" x2="482" y2="672" stroke="#7f93b3" stroke-width="3"/>
    <polygon class="top-notch" points="252,0 327,0 290,56" fill="var(--red)"/>
    <polygon class="top-notch-shade" points="290,0 327,0 290,56" fill="var(--red-dark)" opacity="0.55"/>

    <g class="title-banner">
      <polygon points="172,150 178,145 178,200" fill="var(--red-dark)"/>
      <polygon points="178,145 470,145 492,200 178,200" fill="var(--red)"/>
    </g>

    <g class="list-tabs" fill="var(--red)">
      <polygon points="236,259 300,259 312,283 248,283" fill="var(--navy-deep)" transform="translate(4,3)"/>
      <polygon points="236,259 300,259 312,283 248,283"/>
      <polygon points="272,319 338,319 350,343 284,343" fill="var(--navy-deep)" transform="translate(4,3)"/>
      <polygon points="272,319 338,319 350,343 284,343"/>
      <polygon points="290,381 356,381 368,405 302,405" fill="var(--navy-deep)" transform="translate(4,3)"/>
      <polygon points="290,381 356,381 368,405 302,405"/>
      <polygon points="323,442 390,442 402,466 335,466" fill="var(--navy-deep)" transform="translate(4,3)"/>
      <polygon points="323,442 390,442 402,466 335,466"/>
      <polygon points="355,505 422,505 434,529 367,529" fill="var(--navy-deep)" transform="translate(4,3)"/>
      <polygon points="355,505 422,505 434,529 367,529"/>
      <polygon points="390,568 458,568 470,592 402,592" fill="var(--navy-deep)" transform="translate(4,3)"/>
      <polygon points="390,568 458,568 470,592 402,592"/>
      <polygon points="418,627 476,627 488,651 430,651" fill="var(--navy-deep)" transform="translate(4,3)"/>
      <polygon points="418,627 476,627 488,651 430,651"/>
    </g>
  </svg>

  <div class="mascot-scene" role="img" aria-label="Illustration of the mascot dog beside a toppling stack of archive boxes"></div>

  <div class="brand"><span class="brand-mark"></span><span class="brand-name">Tidy Vault</span></div>

  <h1 class="section-title">PROBLEM</h1>

  <ul class="problem-list">
    <li class="problem-item" style="right:443px; top:375px;">OH&amp;S risks from heavy boxes</li>
    <li class="problem-item" style="right:372px; top:461px;">Inefficient use of space</li>
    <li class="problem-item" style="right:372px; top:549px;">Inability to find records</li>
    <li class="problem-item" style="right:325px; top:636px;">Complicated destruction and retention schedules</li>
    <li class="problem-item" style="right:282px; top:726px;">Collapsing boxes and cluttered rooms</li>
    <li class="problem-item" style="right:228px; top:816px;">No continuity or systems during staff turnover</li>
    <li class="problem-item" style="right:200px; top:900px;">Time-poor administrators</li>
  </ul>
</main>
</body>
</html>
```